Velmora - 3D medical animations and high end visual content

Our company creates high end visual content and animations for medical global companies.
Our website - www.velmora-studio.example
We would like to have an amazing business card for our CEO that he can use in the following exhebitions he is going to attend.
It is very important that the design will be memorable and diffrent. It has to reflect our brand design (you can have it from our website)
We would like to transmit innovation, prestige, luxury, aesthetics.
The card has to be Double Sided

Target Market(s)

Marketing managers in medical global companys

Industry/Entity Type

It Company

Contact Information for Business Card

Requirements
Nice to have
• It is very important that the design will be memorable and diffrent. It has to reflect our brand design (you can have it from our website)

```html
<!DOCTYPE html>
<html lang="en">
<head>
<meta charset="utf-8">
<title>Velmora – Business Card</title>
<link rel="stylesheet" href="https://fonts.googleapis.com/css2?family=Open+Sans:wght@400;600&display=swap">
<style>
  :root {
    --stage: #4b4b4d;
    --teal: #2e9bb3;
    --ink: #2f2f31;
    --grey-line: #9a9a9a;
    --paper: #ffffff;
    --muted: #3a3a3a;
  }
  * { margin: 0; padding: 0; box-sizing: border-box; }
  html, body {
    width: 1200px; height: 977px; overflow: hidden;
    background: var(--stage);
    font-family: "Open Sans", Arial, sans-serif;
  }
  .stage {
    width: 1200px; height: 977px;
    display: flex; flex-direction: column;
    align-items: center; justify-content: center; gap: 50px;
  }
  .card {
    position: relative;
    width: 700px; height: 400px;
    box-shadow: 0 10px 30px rgba(0,0,0,.35);
    overflow: hidden;
  }
  /* Front side */
  .card--front {
    background: var(--teal);
    display: flex; align-items: center; justify-content: center;
  }
  .brand-name {
    font-weight: 600;
    letter-spacing: 4px;
    text-transform: uppercase;
  }
  .card--front .brand-name { color: var(--paper); font-size: 56px; }

  /* Back side */
  .card--back { background: var(--paper); }
  .card--back .brand-name {
    position: absolute; left: 50px; top: 150px;
    color: var(--ink); font-size: 44px;
  }
  .divider {
    position: absolute; left: 330px; top: 42px;
    width: 1px; height: 230px;
    background: linear-gradient(var(--paper), var(--grey-line) 40%, var(--grey-line) 70%, var(--paper));
  }
  .contact {
    position: absolute; left: 372px; top: 50px;
    color: var(--muted);
  }
  .contact__name { color: var(--teal); font-weight: 600; font-size: 22px; letter-spacing: .5px; }
  .contact__title { font-weight: 600; font-size: 13px; color: var(--ink); margin-top: 2px; }
  .contact__list { list-style: none; margin-top: 26px; }
  .contact__item {
    display: flex; align-items: center; gap: 12px;
    font-size: 14px; line-height: 25px;
  }
  .contact__icon { width: 14px; height: 14px; fill: var(--teal); flex: none; }
  .base-bands { position: absolute; left: 0; bottom: 0; width: 700px; height: 80px; }
  .band--dark { fill: var(--ink); }
  .band--teal { fill: var(--teal); }
</style>
</head>
<body>
<main class="stage">
  <section class="card card--front" aria-label="Business card front">
    <span class="brand-name">Velmora</span>
  </section>

  <section class="card card--back" aria-label="Business card back">
    <span class="brand-name">Velmora</span>
    <div class="divider"></div>
    <div class="contact">
      <p class="contact__name">Eran Talmor</p>
      <p class="contact__title">Founder &amp; CEO</p>
      <ul class="contact__list">
        <li class="contact__item">
          <svg class="contact__icon" viewBox="0 0 14 14"><path d="M4 0h6a1 1 0 0 1 1 1v12a1 1 0 0 1-1 1H4a1 1 0 0 1-1-1V1a1 1 0 0 1 1-1zm.5 1.5v9h5v-9zM7 11.3a.8.8 0 1 0 0 1.6.8.8 0 0 0 0-1.6z"/></svg>
          +972-52-5550148
        </li>
        <li class="contact__item">
          <svg class="contact__icon" viewBox="0 0 14 14"><path d="M7 1 0 7.5h2V13h3.8V9.2h2.4V13H12V7.5h2z"/></svg>
          +972-77-5550193
        </li>
        <li class="contact__item">
          <svg class="contact__icon" viewBox="0 0 14 14"><path d="M0 3h14v1L7 8.5 0 4zm0 2.3 7 4.5 7-4.5V12H0z"/></svg>
          eran@velmora-studio.example
        </li>
        <li class="contact__item">
          <svg class="contact__icon" viewBox="0 0 14 14"><path d="M7 0a7 7 0 1 0 0 14A7 7 0 0 0 7 0zm0 1.2c.8 0 1.7 1.6 2 4.2H5c.3-2.6 1.2-4.2 2-4.2zM1.3 6.6h2.5c0 .3 0 .6.1.9H1.3a5 5 0 0 1 0-.9zm3.7 0h4c0 .3 0 .6-.1.9H5zm5.2 0h2.5v.9h-2.6zM1.6 8.7h2.5c.2 1.4.6 2.6 1.1 3.4a5.8 5.8 0 0 1-3.6-3.4zm3.7 0h3.4c-.3 2-1 3.2-1.7 3.2S5.6 10.7 5.3 8.7zm4.6 0h2.5a5.8 5.8 0 0 1-3.6 3.4c.5-.8.9-2 1.1-3.4z"/></svg>
          www.velmora-studio.example
        </li>
      </ul>
    </div>
    <svg class="base-bands" viewBox="0 0 700 80" aria-hidden="true">
      <polygon class="band--dark" points="0,52 130,52 150,80 0,80"/>
      <polygon class="band--teal" points="142,52 598,52 616,80 162,80"/>
      <polygon class="band--teal" points="606,36 616,36 608,52 598,52"/>
      <polygon class="band--dark" points="618,20 700,20 700,80 630,80"/>
    </svg>
  </section>
</main>
</body>
</html>
```